Business Card Design

we are Koorawatha Orchards & we would like a business card that stands out from the crowd and that we can apply this design to our products as we will be also placing orders for labels and stickers in the future

Industry/Entity Type

Business

Contact Information for Business Card

Packing Shed : 54 917 360
mobile : 0428 351 904
email : koorawathaorchards@fernmail.net.au
address : Pelican Crescent Tarrawong 4578

```html
<!DOCTYPE html>
<html lang="en">
<head>
<meta charset="utf-8">
<title>Koorawatha Orchards – Business Card</title>
<link rel="stylesheet" href="https://fonts.googleapis.com/css2?family=PT+Sans:wght@400;700&display=swap">
<style>
  :root {
    --backdrop: #3a3a38;
    --card-white: #ffffff;
    --sunny-yellow: #fff200;
    --deep-yellow: #f2e000;
    --berry-red: #e3202a;
    --ink: #111111;
  }
  * { margin: 0; padding: 0; box-sizing: border-box; }
  html, body {
    width: 1200px;
    height: 677px;
    overflow: hidden;
    background: var(--backdrop);
    font-family: "PT Sans", sans-serif;
  }
  .stage {
    position: relative;
    width: 1200px;
    height: 677px;
  }
  .card {
    position: absolute;
    top: 196px;
    width: 500px;
    height: 286px;
    background: var(--card-white);
    overflow: hidden;
  }
  .card-front { left: 70px; }
  .card-back { left: 630px; }

  /* Front */
  .front-wave {
    position: absolute;
    left: 0;
    top: 0;
    width: 500px;
    height: 286px;
  }
  .brand {
    position: absolute;
    display: flex;
    align-items: center;
    gap: 14px;
  }
  .brand-mark {
    border-radius: 50%;
    background: var(--berry-red);
    flex: none;
  }
  .brand-name {
    color: var(--berry-red);
    font-weight: 700;
    white-space: nowrap;
  }
  .front-brand { left: 34px; top: 30px; }
  .front-brand .brand-mark { width: 58px; height: 58px; }
  .front-brand .brand-name { font-size: 23px; }

  .contact-list {
    position: absolute;
    left: 34px;
    top: 176px;
    display: grid;
    grid-template-columns: 112px auto;
    row-gap: 1px;
    color: var(--ink);
  }
  .contact-label {
    font-size: 17px;
    font-weight: 700;
    line-height: 20px;
  }
  .contact-value {
    font-size: 13.5px;
    font-weight: 700;
    line-height: 20px;
  }

  /* Back */
  .band {
    position: absolute;
    left: 0;
    width: 100%;
    background: var(--sunny-yellow);
  }
  .band-top { top: 0; height: 30px; }
  .band-bottom { bottom: 0; height: 42px; }
  .back-brand {
    left: 0;
    right: 0;
    top: 104px;
    justify-content: center;
  }
  .back-brand .brand-mark { width: 62px; height: 62px; }
  .back-brand .brand-name { font-size: 28px; }
</style>
</head>
<body>
<main class="stage">

  <section class="card card-front" aria-label="Business card front">
    <svg class="front-wave" viewBox="0 0 500 286" aria-hidden="true">
      <path d="M0 150 Q250 95 500 118 L500 286 L0 286 Z" fill="var(--sunny-yellow)"/>
      <path d="M0 150 Q250 95 500 118" fill="none" stroke="var(--card-white)" stroke-width="5"/>
      <path d="M0 158 Q250 104 500 126" fill="none" stroke="var(--deep-yellow)" stroke-width="2"/>
    </svg>
    <div class="brand front-brand">
      <span class="brand-mark"></span>
      <span class="brand-name">Koorawatha Orchards</span>
    </div>
    <dl class="contact-list">
      <dt class="contact-label">Packing Shed</dt><dd class="contact-value">: 54 917 360</dd>
      <dt class="contact-label">Mobile</dt><dd class="contact-value">: 0428 351 904</dd>
      <dt class="contact-label">Email</dt><dd class="contact-value">: koorawathaorchards@fernmail.net.au</dd>
      <dt class="contact-label">Address</dt><dd class="contact-value">: Pelican Crescent Tarrawong 4578</dd>
    </dl>
  </section>

  <section class="card card-back" aria-label="Business card back">
    <div class="band band-top"></div>
    <div class="brand back-brand">
      <span class="brand-mark"></span>
      <span class="brand-name">Koorawatha Orchards</span>
    </div>
    <div class="band band-bottom"></div>
  </section>

</main>
</body>
</html>
```